Veltrane Business Card - Construction Management

Create a business card for a construction management firm that owns/responsible for three other companies and include the following:
Main Company & Logo - Veltrane Management Group Ltd.
Subsidiary Company Logo only to appear on card in miniature form :
Quelbrin Industrial Services Ltd.
Halvoran Sisters Construction Inc.
Tessaly Groundworks

Contact Information for Business Card

Veltrane Management Group Ltd.
872 Brelford Road - Coville Industrial Park
RM of Danbrook
Regina, Saskatchewan
S7T 2B9
P: 306.555.0182
C: 306.555.0147
e:jtorvelli@veltrane-example.ca

Colors

Designer to choose colors to be used in the design.

Requirements
Must have
• Main Logo and small/miniature version of three subsidiary company logos.
• We would appreciate seeing a version of main logo(Veltrane Group) on front of card and other three miniature/small logos on the front of the card or version of main logo on front and other three logos on the back of the card.

```html
<!DOCTYPE html>
<html lang="en">
<head>
<meta charset="utf-8">
<title>Veltrane Business Card</title>
<link href="https://fonts.googleapis.com/css2?family=Roboto:wght@400;500;700&family=Roboto+Condensed:wght@700&display=swap" rel="stylesheet">
<style>
  :root {
    --backdrop: #2f2f31;
    --brand-blue: #1273bb;
    --brand-gray: #7d7e80;
    --paper: #f1f1f1;
    --ink-white: #ffffff;
    --card-black: #1d1e20;
  }
  * { box-sizing: border-box; margin: 0; padding: 0; }
  html, body {
    width: 1200px; height: 960px; overflow: hidden;
    background: var(--backdrop);
    font-family: "Roboto", Arial, sans-serif;
  }
  .card {
    position: absolute; width: 600px; height: 342px; overflow: hidden;
    box-shadow: 0 4px 10px rgba(0,0,0,.45);
  }
  .card-front { left: 313px; top: 113px; background: var(--paper); }
  .card-back { left: 312px; top: 473px; background: var(--card-black); }

  .front-shape { position: absolute; inset: 0; }
  .contact-block {
    position: absolute; left: 30px; top: 52px; color: var(--ink-white);
  }
  .person-name { font-size: 24px; font-weight: 500; letter-spacing: .5px; line-height: 28px; }
  .person-title { font-size: 16px; font-weight: 400; line-height: 20px; margin-bottom: 16px; }
  .company-name {
    font-family: "Roboto Condensed", Arial, sans-serif;
    font-weight: 700; font-size: 13.5px; line-height: 18px;
  }
  .address, .phones { font-size: 14px; line-height: 19px; }
  .address { margin-bottom: 8px; }
  .web { letter-spacing: 1.4px; }

  .brand-lockup {
    position: absolute; left: 326px; top: 145px;
    display: flex; align-items: center; gap: 10px;
  }
  .brand-square { width: 54px; height: 54px; background: var(--brand-blue); }
  .brand-name {
    font-family: "Roboto Condensed", Arial, sans-serif; font-weight: 700;
    font-size: 22px; line-height: 24px; color: var(--brand-blue);
    text-transform: uppercase;
  }

  .back-brand {
    position: absolute; left: 0; right: 0; top: 82px;
    display: flex; flex-direction: column; align-items: center; gap: 14px;
  }
  .back-square { width: 110px; height: 110px; background: var(--brand-blue); }
  .back-name {
    font-family: "Roboto Condensed", Arial, sans-serif; font-weight: 700;
    font-size: 26px; color: var(--brand-blue); text-transform: uppercase;
    letter-spacing: 1px;
  }
  .subsidiaries {
    position: absolute; left: 0; right: 0; top: 276px;
    display: flex; justify-content: center; gap: 26px;
  }
  .subsidiary {
    font-family: "Roboto Condensed", Arial, sans-serif; font-weight: 700;
    font-size: 10px; line-height: 12px; color: var(--ink-white);
    text-align: center; text-transform: uppercase; max-width: 90px;
  }
</style>
</head>
<body>
  <section class="card card-front">
    <svg class="front-shape" width="600" height="342" viewBox="0 0 600 342">
      <polygon points="0,0 352,0 267,187 357,342 0,342" fill="var(--brand-blue)"/>
      <polygon points="352,0 364,0 279,187 369,342 357,342 267,187" fill="var(--brand-gray)"/>
    </svg>
    <div class="contact-block">
      <p class="person-name">JORDAN TORVELLI</p>
      <p class="person-title">CEO/FOUNDER</p>
      <p class="company-name">Veltrane Management Group Ltd.</p>
      <p class="address">872 Brelford Road - Coville<br>Industrial Park, RM of Danbrook<br>Regina, Saskatchewan, S7T 2B9</p>
      <p class="phones">Phone: 306.555.0182<br>Mob: 306.555.0147<br>jtorvelli@veltrane-example.ca<br><span class="web">www.veltrane-example.ca</span></p>
    </div>
    <div class="brand-lockup">
      <span class="brand-square"></span>
      <span class="brand-name">Veltrane<br>Group</span>
    </div>
  </section>

  <section class="card card-back">
    <div class="back-brand">
      <span class="back-square"></span>
      <span class="back-name">Veltrane Group</span>
    </div>
    <div class="subsidiaries">
      <span class="subsidiary">Halvoran Sisters Construction</span>
      <span class="subsidiary">Quelbrin Industrial</span>
      <span class="subsidiary">Tessaly Groundworks</span>
    </div>
  </section>
</body>
</html>
```